Website Design for Forklift Training Company

DO NOT CONTACT PRIVATELY. ONLY SUBMISSIONS HERE WILL BE CONSIDERED

I need a design for a website that offers forklift training courses.

The company offers accredited, onsite forklift training that are customized for the needs of each individual company. The company offers a variety of courses to operate forklifts and other machinary.

About: "Pembrook Lift Academy Ltd delivers bespoke onsite forklift truck operator training throught the uk.
All our instructors have a wealth of knowledge and expertise to provide your company with all your forklift truck training requirements.
Pembrook Lift Academy Ltd is registered and accredited by qkmvd standards so you can be rest assured that all forklift training is carried out the very highest standard"

I need the following pages designed:
> a) Home Page: Include a header image, ways to contact, about snippet, overview of courses, accreditation that will be received after completing the courses. (See attachments for samples)
> b) About Page
> c) Contact Us Page
> d) Course Page Template: A page that will be used as template for the courses offered. It should contain;
1. Cover image for the course
2. A description of the course
3. A table indicating the various course options
4. Course Objectives
5. What the trainee will receive after doing the course (example: a certification)

Target Market(s)

Industrial Businesses

Number of Pages Required

4 page

Colors
0054AA
0677BA
7BADD7
CADEEF
E8F1F8
0094D4
00A9DD
6FCCEA
C7EBF8
E9F6FB

Requirements
Should not have
• - No Search bar

```html
<!DOCTYPE html>
<html lang="en">
<head>
<meta charset="utf-8">
<title>Pembrook Lift Academy Ltd – Forklift Training Courses</title>
<link rel="stylesheet" href="https://fonts.googleapis.com/css2?family=Rajdhani:wght@500;600;700&family=Playfair+Display:wght@400;600&family=Raleway:wght@400;500;600&family=Roboto+Condensed:wght@400&display=swap">
<style>
:root{
  --blue-deep:#0054AA;
  --blue-mid:#0677BA;
  --blue-soft:#7BADD7;
  --blue-pale:#CADEEF;
  --blue-mist:#E8F1F8;
  --cyan:#0094D4;
  --cyan-bright:#00A9DD;
  --cyan-soft:#6FCCEA;
  --cyan-pale:#C7EBF8;
  --cyan-mist:#E9F6FB;
  --ink:#1b1f24;
  --text:#5d636a;
  --navy:#0a2336;
  --footer:#0d1a26;
  --white:#ffffff;
  --head:"Rajdhani",sans-serif;
  --serif:"Playfair Display",serif;
  --body:"Raleway",sans-serif;
  --nav:"Roboto Condensed",sans-serif;
}
*{margin:0;padding:0;box-sizing:border-box}
html,body{width:1200px;height:3557px;overflow:hidden}
body{position:relative;background:var(--white);font-family:var(--body);color:var(--text)}
.abs{position:absolute}
.btn{position:absolute;display:flex;align-items:center;justify-content:center;background:linear-gradient(var(--cyan),var(--blue-mid));color:var(--white);font-family:var(--head);font-weight:700;font-size:13px;letter-spacing:.3px;text-transform:uppercase}
.section-title{position:absolute;left:0;width:1200px;text-align:center;font-family:var(--head);font-weight:700;font-size:34px;color:var(--ink);letter-spacing:.5px}

/* top bar */
.topbar{left:0;top:0;width:1200px;height:32px;background:var(--cyan)}
.topbar-phone{left:112px;top:8px;color:var(--white);font-size:12px;display:flex;align-items:center;gap:5px}
.topbar-social{right:112px;top:9px;display:flex;gap:12px}
.dot{width:14px;height:14px;border-radius:50%;border:2px solid var(--white)}

/* hero */
.hero{left:0;top:32px;width:1200px;height:618px;background:linear-gradient(90deg,#2a2e33 0%,#3b3a36 25%,#1d4567 55%,#0d5f98 72%,#e7d84a 82%,#c9c04a 100%)}
.hero-shade{left:0;top:32px;width:620px;height:618px;background:linear-gradient(90deg,rgba(10,20,30,.55),rgba(10,20,30,0))}
.headerbar{left:0;top:32px;width:1200px;height:59px;background:rgba(8,26,44,.55)}
.logo{display:flex;align-items:center;gap:8px;font-family:var(--head);font-weight:700;font-size:19px;color:var(--white);letter-spacing:.3px}
.logo-mark{width:20px;height:20px;background:var(--white)}
.nav{top:54px;display:flex;font-family:var(--nav);font-size:13px;color:var(--white);text-transform:uppercase}
.nav span{position:absolute;white-space:nowrap}
.nav .active{color:var(--cyan-soft)}
.hero-kicker{left:112px;top:229px;color:var(--white);font-size:21px;font-weight:500}
.hero-title{left:112px;top:250px;color:var(--white);font-family:var(--serif);font-size:52px;font-weight:600}
.hero-text{left:112px;top:324px;width:410px;color:var(--white);font-size:14px;line-height:22px}
.circle-arrow{position:absolute;border-radius:50%;border:1.5px solid var(--white);display:flex;align-items:center;justify-content:center}

/* about */
.about-band{left:112px;top:650px;width:174px;height:402px;background:linear-gradient(180deg,var(--cyan-bright),var(--blue-deep))}
.about-image{left:131px;top:704px;width:395px;height:276px;background:linear-gradient(90deg,rgba(240,244,247,0) 0%,#e9ecef 30%,#c8ccd0 55%,#e98a4c 75%,#f3f4f5 100%)}
.about-kicker{left:532px;top:721px;font-size:14px;color:#333;font-weight:500}
.about-title{left:532px;top:742px;font-family:var(--head);font-weight:700;font-size:31px;color:var(--ink)}
.about-text{left:532px;top:796px;width:555px;font-size:14px;line-height:22px}
.about-text p+p{margin-top:8px}

/* categories */
.cat-band{left:0;top:1109px;width:1200px;height:251px;background:linear-gradient(180deg,rgba(0,84,170,.92),rgba(6,60,120,.95)),linear-gradient(90deg,#0b3a6a,#16659b,#0b3a6a)}
.cat-sep{top:1157px;width:1px;height:152px;background:rgba(255,255,255,.25)}
.cat{top:1175px;width:333px;text-align:center;color:var(--white);font-family:var(--serif);font-size:21px;font-weight:600}
.cat svg{display:block;margin:0 auto 14px}

/* course grid */
.card{position:absolute;width:224px;height:163px;background:var(--cyan-mist);border:1px solid var(--cyan-pale);text-align:center;font-family:var(--serif);font-size:16px;line-height:25px;color:var(--ink)}
.card svg{display:block;margin:30px auto 10px}
.card.active{background:var(--cyan-bright);color:var(--white);border-color:var(--cyan-bright);box-shadow:0 4px 10px rgba(0,100,160,.25)}

/* tiles */
.tile{position:absolute;width:308px;height:229px;overflow:hidden}
.tile-photo{position:absolute;inset:0}
.tile-caption{position:absolute;left:0;bottom:0;width:100%;height:44px;background:rgba(0,148,212,.78);color:var(--white);font-family:var(--serif);font-size:15px;padding:12px 17px}
.tile-feature{background:linear-gradient(180deg,rgba(0,169,221,.88),rgba(6,119,186,.92)),#1f6f9e;color:var(--white);text-align:center;padding:38px 22px 0}
.tile-feature h3{font-family:var(--serif);font-weight:600;font-size:21px;line-height:22px}
.tile-feature p{font-size:12.5px;line-height:19px;margin-top:12px}
.tile-feature a{display:inline-block;margin-top:12px;font-family:var(--head);font-weight:700;font-size:13px;color:var(--white);text-decoration:underline}

/* accreditation */
.badge{left:550px;top:2607px;width:118px;height:75px;border-radius:6px;background:var(--blue-mist);border:2px solid var(--blue-soft)}
.accr-text{left:112px;top:2706px;width:976px;text-align:center;font-size:14.5px;line-height:25px}
.round-arrow{position:absolute;width:42px;height:42px;border-radius:50%;border:1px solid #8a9096;display:flex;align-items:center;justify-content:center}

/* cta */
.cta-band{left:0;top:2910px;width:1200px;height:312px;background:linear-gradient(90deg,#0a1d2e,#0b2a44)}
.cta-title{left:112px;top:2988px;font-family:var(--head);font-weight:700;font-size:34px;color:var(--white)}
.cta-text{left:112px;top:3034px;width:380px;font-size:15px;line-height:22px;color:var(--white)}
.callback{left:696px;top:2881px;width:392px;height:291px;background:#16b9ec}
.callback-title{left:696px;top:2911px;width:392px;text-align:center;font-family:var(--head);font-weight:700;font-size:20px;color:var(--white)}
.field{position:absolute;left:728px;width:329px;height:39px;background:var(--white);border:1px solid var(--blue-pale);font-size:11px;color:#444;padding:12px 10px}
.btn-navy{background:linear-gradient(var(--blue-mid),var(--blue-deep))}

/* footer */
.footer{left:0;top:3222px;width:1200px;height:335px;background:var(--footer)}
.foot-h{top:3266px;font-family:var(--head);font-weight:700;font-size:17px;color:var(--white)}
.foot-text{font-size:11px;line-height:19px;color:var(--blue-pale)}
.foot-list{top:3300px;font-size:11px;color:var(--blue-pale)}
.foot-list li{list-style:none;height:27.5px}
.contact-row{position:absolute;display:flex;gap:8px;font-size:11px;line-height:15px;color:var(--blue-pale)}
.social-round{position:absolute;top:3461px;width:30px;height:30px;border-radius:50%;border:1px solid var(--blue-soft);display:flex;align-items:center;justify-content:center}
.social-round i{width:8px;height:8px;border-radius:50%;background:var(--white)}
.copyright{left:0;top:3499px;width:1200px;text-align:center;font-size:10px;color:var(--cyan-bright)}
.copyright b{color:var(--white);font-weight:500}
</style>
</head>
<body>

<!-- top bar -->
<div class="abs topbar"></div>
<div class="abs topbar-phone">
  <svg width="10" height="12" viewBox="0 0 10 12"><path d="M2 1 L4 1 L4.5 3.5 L3.3 4.3 Q4.3 7 6.5 8.5 L7.5 7.4 L9.5 8 L9.5 10 Q9 11 7.5 11 Q1 9 1 2 Q1 1 2 1Z" fill="#fff"/></svg>
  +44 7700 900418
</div>
<div class="abs topbar-social"><span class="dot"></span><span class="dot"></span></div>

<!-- hero -->
<div class="abs hero" role="img" aria-label="Warehouse with a yellow forklift and a smiling instructor in a high-visibility vest giving a thumbs up"></div>
<div class="abs hero-shade"></div>
<div class="abs headerbar"></div>
<div class="abs logo" style="left:112px;top:51px"><span class="logo-mark"></span>PEMBROOK LIFT ACADEMY LTD</div>
<nav class="abs nav" style="left:0;width:1200px">
  <span class="active" style="left:699px">Home</span>
  <span style="left:783px">About</span>
  <span style="left:870px">Traing Course</span>
  <span style="left:1014px">Contact Us</span>
</nav>
<div class="abs hero-kicker">FORKLIFT</div>
<h1 class="abs hero-title">Training Courses</h1>
<p class="abs hero-text">Pembrook Lift Academy Ltd delivers bespoke onsite forklift truck training courses accredited by qkmvd nationwide 24/7 at your premises</p>
<div class="btn" style="left:112px;top:407px;width:116px;height:42px">Contact Us</div>
<div class="circle-arrow" style="left:565px;top:589px;width:33px;height:33px"><svg width="8" height="10"><path d="M6 1 L2 5 L6 9" stroke="#fff" fill="none" stroke-width="1.5"/></svg></div>
<div class="circle-arrow" style="left:603px;top:589px;width:33px;height:33px"><svg width="8" height="10"><path d="M2 1 L6 5 L2 9" stroke="#fff" fill="none" stroke-width="1.5"/></svg></div>

<!-- about -->
<div class="abs about-band"></div>
<div class="abs about-image" role="img" aria-label="Orange and grey counterbalance forklift truck with lowered forks"></div>
<div class="abs about-kicker">ABOUT</div>
<h2 class="abs about-title">PEMBROOK LIFT ACADEMY LTD</h2>
<div class="abs about-text">
  <p>Pembrook Lift Academy Ltd delivers bespoke onsite forklift truck operator training throught the uk. All our instructors have a wealth of knowledge and expertise to provide your company with all your forklift truck training requirements.</p>
  <p>Pembrook Lift Academy Ltd is registered and accredited by qkmvd standards so you can be rest assured that all forklift training is carried out the very highest standard</p>
</div>
<div class="btn" style="left:532px;top:939px;width:116px;height:40px">Read More</div>

<!-- categories -->
<div class="abs cat-band" role="img" aria-label="Blue-tinted photo of an operator in a hard hat working in a warehouse"></div>
<div class="abs cat-sep" style="left:434px"></div>
<div class="abs cat-sep" style="left:767px"></div>
<div class="abs cat" style="left:100px">
  <svg width="76" height="60" viewBox="0 0 76 60" fill="none" stroke="#fff" stroke-width="3"><path d="M6 46 V22 H22 L30 38 H40 V46Z"/><path d="M40 6 V50 H60"/><rect x="50" y="20" width="12" height="12"/><rect x="50" y="34" width="12" height="12"/><circle cx="14" cy="50" r="5"/><circle cx="32" cy="50" r="5"/></svg>
  Forklift Training Courses
</div>
<div class="abs cat" style="left:434px">
  <svg width="70" height="60" viewBox="0 0 70 60" fill="none" stroke="#fff" stroke-width="3"><path d="M8 6 H36 M10 6 V14 M34 6 V14"/><path d="M22 14 L58 28"/><path d="M10 32 H58 V44 H10Z"/><circle cx="20" cy="50" r="6"/><circle cx="48" cy="50" r="6"/></svg>
  Mewp Training Courses
</div>
<div class="abs cat" style="left:767px">
  <svg width="64" height="60" viewBox="0 0 64 60" fill="none" stroke="#fff" stroke-width="3"><path d="M8 2 V52 H60"/><path d="M16 12 V44 H52 V26"/><path d="M44 12 H58 M51 5 V19"/></svg>
  Other Training Courses
</div>

<!-- forklift courses -->
<h2 class="section-title" style="top:1407px">FORKLIFT TRAINING COURSES</h2>

<div class="card" style="left:112px;top:1464px"><svg width="52" height="42" viewBox="0 0 52 42" fill="#0b4f7a"><path d="M4 8 H26 L34 20 H48 V34 H4Z"/><circle cx="13" cy="36" r="5" fill="#fff" stroke="#0b4f7a" stroke-width="3"/><circle cx="39" cy="36" r="5" fill="#fff" stroke="#0b4f7a" stroke-width="3"/></svg>Veyra<br>Truck Training Course</div>
<div class="card active" style="left:363px;top:1464px"><svg width="52" height="42" viewBox="0 0 52 42" fill="#fff"><rect x="6" y="16" width="22" height="16"/><rect x="32" y="4" width="4" height="32"/><rect x="38" y="8" width="10" height="10"/><rect x="38" y="22" width="10" height="10"/><circle cx="12" cy="36" r="4"/><circle cx="24" cy="36" r="4"/></svg>Duolift<br>Lift Training course</div>
<div class="card" style="left:613px;top:1464px"><svg width="52" height="42" viewBox="0 0 52 42" fill="#0b4f7a"><path d="M8 6 H28 V30 H8Z"/><rect x="32" y="2" width="5" height="36"/><rect x="37" y="34" width="12" height="4"/><circle cx="14" cy="34" r="5"/></svg>Counterbalance<br>Training Course</div>
<div class="card" style="left:863px;top:1464px"><svg width="52" height="42" viewBox="0 0 52 42" fill="#0b4f7a"><rect x="4" y="4" width="20" height="14"/><path d="M4 20 H34 L44 28 V34 H4Z"/><circle cx="12" cy="36" r="5"/><circle cx="36" cy="36" r="5"/></svg>Pivota<br>Truck Training Course</div>

<div class="card" style="left:112px;top:1656px"><svg width="52" height="42" viewBox="0 0 52 42" fill="#0b4f7a"><rect x="10" y="2" width="12" height="14"/><path d="M6 18 H30 V32 H6Z"/><rect x="32" y="10" width="10" height="22"/><rect x="6" y="34" width="26" height="6" rx="3"/></svg>Kranex<br>Crane Training Course</div>
<div class="card" style="left:363px;top:1656px"><svg width="52" height="42" viewBox="0 0 52 42" fill="#0b4f7a"><rect x="16" y="4" width="14" height="16"/><path d="M4 20 H48 V30 H4Z"/><circle cx="12" cy="34" r="6"/><circle cx="38" cy="34" r="6"/></svg>Llop<br>Training Course</div>
<div class="card" style="left:613px;top:1656px"><svg width="52" height="42" viewBox="0 0 52 42" fill="#0b4f7a"><rect x="4" y="4" width="8" height="26"/><rect x="14" y="10" width="12" height="20"/><path d="M28 20 H46 V32 H28Z"/><circle cx="10" cy="36" r="4"/><circle cx="34" cy="36" r="4"/><circle cx="44" cy="36" r="4"/></svg>Mountra<br>Truck Training Course</div>
<div class="card" style="left:863px;top:1656px"><svg width="52" height="42" viewBox="0 0 52 42" fill="#0b4f7a"><rect x="6" y="2" width="16" height="10"/><rect x="6" y="14" width="16" height="10"/><rect x="6" y="26" width="16" height="10"/><rect x="26" y="4" width="4" height="32"/><path d="M32 22 H46 V34 H32Z"/><circle cx="38" cy="38" r="3"/></svg>Order Picker<br>Truck Training Course</div>

<div class="btn" style="left:504px;top:1850px;width:192px;height:42px">View All Courses</div>

<!-- other courses -->
<h2 class="section-title" style="top:1940px">OTHER TRAINING COURSES</h2>

<div class="tile tile-feature" style="left:112px;top:1993px">
  <h3>Skidmaster<br>Truck Training Course</h3>
  <p>Skid loaders are essential in the workplace and are operated throughout the world in warehouses, construction sites, factories and many more places.</p>
  <a>READ MORE</a>
</div>
<div class="tile" style="left:446px;top:1993px"><div class="tile-photo" role="img" aria-label="Operator driving an orange forklift beside stacked wooden pallets" style="background:linear-gradient(90deg,#a48a68,#8f9298 40%,#e06b3a 70%,#9ea3a8)"></div><div class="tile-caption">Skidmaster Truck Training Course</div></div>
<div class="tile" style="left:780px;top:1993px"><div class="tile-photo" role="img" aria-label="Lorry-mounted crane lifting a bulk bag under a blue sky" style="background:linear-gradient(180deg,#5b86c8,#8aa7cf 45%,#6b6a55 75%,#444a40)"></div><div class="tile-caption">Skidmaster Truck Training Course</div></div>
<div class="tile" style="left:112px;top:2248px"><div class="tile-photo" role="img" aria-label="Orange skid steer loader parked in a workshop" style="background:linear-gradient(90deg,#7a2b2b,#3a3d40 35%,#d9862a 60%,#3b3835)"></div><div class="tile-caption">Skidmaster Truck Training Course</div></div>
<div class="tile" style="left:446px;top:2248px"><div class="tile-photo" role="img" aria-label="Orange forklift between stacks of bagged material under a cloudy sky" style="background:linear-gradient(180deg,#c4ccd6,#a6957a 45%,#d77a3b 70%,#6d6558)"></div><div class="tile-caption">Skidmaster Truck Training Course</div></div>
<div class="tile" style="left:780px;top:2248px"><div class="tile-photo" role="img" aria-label="Yellow forklift inside a steel warehouse with coils" style="background:linear-gradient(180deg,#5f6a72,#3d464d 40%,#c9b93a 70%,#6f7478)"></div><div class="tile-caption">Skidmaster Truck Training Course</div></div>

<!-- accreditation -->
<h2 class="section-title" style="top:2532px">TRAINING ACCREDITATION</h2>
<div class="abs badge"></div>
<p class="abs accr-text">We are accredited by the qkmvd who are recognised by the workplace safety council as competent to deliver forklift truck operator training courses. As an qkmvd accredited training provider we are monitored annually to ensure we are maintaining our high standards as laid down by the qkmvd.<br>All our instructors are qualified and registered with the qkmvd and monitored. Please note we are only accredited to deliver training at customer premises as we do not have a training centre.</p>
<div class="round-arrow" style="left:34px;top:2748px"><svg width="8" height="12"><path d="M6 1 L2 6 L6 11" stroke="#333" fill="none" stroke-width="1.5"/></svg></div>
<div class="round-arrow" style="left:1122px;top:2748px"><svg width="8" height="12"><path d="M2 1 L6 6 L2 11" stroke="#333" fill="none" stroke-width="1.5"/></svg></div>

<!-- call to action -->
<div class="abs cta-band"></div>
<h2 class="abs cta-title">TALK TO OUR TEAM TODAY</h2>
<p class="abs cta-text">We Pride Ourselves On Delivering A Prompt, Reliable And Helpful Service</p>
<div class="btn" style="left:109px;top:3096px;width:117px;height:39px">Contact Us</div>

<div class="abs callback"></div>
<div class="abs callback-title">REQUEST A CALLBACK</div>
<div class="field" style="top:2951px">Name:</div>
<div class="field" style="top:2998px">Email:</div>
<div class="field" style="top:3046px">Phone:</div>
<div class="btn btn-navy" style="left:728px;top:3098px;width:139px;height:38px">Submit Requst</div>

<!-- footer -->
<div class="abs footer"></div>
<div class="abs foot-h" style="left:112px">ABOUT US</div>
<p class="abs foot-text" style="left:112px;top:3298px;width:310px">We specialise in onsite forklift training using the equipment and facilities your employees will use in there everyday work wether its counterbalance mounted reach cherry picker to name a few.</p>
<div class="abs logo" style="left:112px;top:3401px;font-size:18px"><span class="logo-mark"></span>PEMBROOK LIFT ACADEMY LTD</div>

<div class="abs foot-h" style="left:507px">SITEMAP</div>
<ul class="abs foot-list" style="left:507px"><li>Home</li><li>About</li><li>Training Curses</li><li>Contact Us</li></ul>

<div class="abs foot-h" style="left:700px">CONTACTS</div>
<div class="contact-row" style="left:700px;top:3300px"><svg width="10" height="13" viewBox="0 0 10 13"><path d="M5 0 A5 5 0 0 1 10 5 C10 8 5 13 5 13 C5 13 0 8 0 5 A5 5 0 0 1 5 0Z" fill="#00A9DD"/><circle cx="5" cy="5" r="2" fill="#0d1a26"/></svg><span>14 Harrow Lane, Eastfield, Kelby<br>KL4 2XR, United Kingdom</span></div>
<div class="contact-row" style="left:700px;top:3356px"><svg width="10" height="12" viewBox="0 0 10 12"><path d="M2 1 L4 1 L4.5 3.5 L3.3 4.3 Q4.3 7 6.5 8.5 L7.5 7.4 L9.5 8 L9.5 10 Q9 11 7.5 11 Q1 9 1 2 Q1 1 2 1Z" fill="#00A9DD"/></svg><span>+44 7700 900418</span></div>
<div class="contact-row" style="left:700px;top:3396px"><svg width="12" height="9" viewBox="0 0 12 9"><rect width="12" height="9" fill="#00A9DD"/><path d="M0 0 L6 5 L12 0" stroke="#0d1a26" fill="none"/></svg><span>hello@pembrooklift.com</span></div>

<div class="abs foot-h" style="left:994px">LINKS</div>
<ul class="abs foot-list" style="left:994px"><li>Qkmvd</li><li>Sfa</li><li>Prime Step</li><li>Foot Care Service</li><li>Pembrook Lift Academy Ltd</li></ul>

<div class="social-round" style="left:565px"><i></i></div>
<div class="social-round" style="left:604px"><i></i></div>
<p class="abs copyright">COPYRIGHT © 2021 <b>PEMBROOK LIFT ACADEMY LTD</b>. ALL RIGHTS RESERVED.</p>

</body>
</html>
```